RB Cargonet businesscard project

RB Cargonet Ltd is a freshly founded small (3 employees), young (average age is 30 years) company, living from the road transportation market without own tools.
We would like to have an impressive, new-line, cool busines card for a freshly founded forwarding company on an overcrowded market which raises attention and makes the potential partners eager to work with us.

Our logo is in the attachment, please use it for the card.

Target Market(s)

The main profile of the company is logistic/forwarding on road.

Industry/Entity Type

Freight Forwarding

Contact Information for Business Card

Name: Varga Edina
Title: general manager
mobile nr: +36-70/482-5910
fax nr: +36-1/655-3947
e-mail: edina.varga@rbcargonet-example.com
info@rbcargonet-example.com
website address: http://www.rbcargonet-example.com
and if possible maybe some funny or helpful info on the back

Requirements
Must have
• contact details above
Nice to have
• some really nice and catching back-side (info, graphics, useful tool info... anything)
Should not have
• trucks, road, ship, airplane on it...

```html
<!DOCTYPE html>
<html lang="en">
<head>
<meta charset="utf-8">
<title>RB Cargonet – Business Card</title>
<link href="https://fonts.googleapis.com/css2?family=Open+Sans:wght@400;600;700&display=swap" rel="stylesheet">
<style>
  :root {
    --card-bg: #000000;
    --brand-blue: #5b84bf;
    --icon-blue: #4f7ab3;
    --text-white: #ffffff;
    --divider: #3a3a3a;
  }
  html, body {
    margin: 0;
    padding: 0;
    width: 1200px;
    height: 741px;
    overflow: hidden;
    background: var(--card-bg);
  }
  .card {
    position: relative;
    width: 1200px;
    height: 741px;
    background: var(--card-bg);
    font-family: "Open Sans", Arial, sans-serif;
    color: var(--text-white);
  }
  .brand {
    position: absolute;
    left: 60px;
    top: 168px;
    width: 506px;
    display: flex;
    flex-direction: column;
    align-items: center;
  }
  .brand-square {
    width: 170px;
    height: 170px;
    background: var(--brand-blue);
  }
  .brand-name {
    margin-top: 62px;
    font-size: 64px;
    font-weight: 600;
    line-height: 1;
    color: var(--text-white);
    white-space: nowrap;
  }
  .divider {
    position: absolute;
    left: 562px;
    top: 210px;
    width: 1px;
    height: 315px;
    background: linear-gradient(to bottom, transparent, var(--divider) 20%, var(--divider) 80%, transparent);
  }
  .person {
    position: absolute;
    left: 644px;
    top: 184px;
  }
  .person-name {
    margin: 0;
    font-size: 39px;
    font-weight: 700;
    line-height: 1.2;
    color: var(--brand-blue);
  }
  .person-title {
    margin: 2px 0 0;
    font-size: 29px;
    font-weight: 400;
    line-height: 1.2;
  }
  .contacts {
    position: absolute;
    left: 644px;
    top: 336px;
    margin: 0;
    padding: 0;
    list-style: none;
  }
  .contact-item {
    display: flex;
    align-items: center;
    height: 43.5px;
    font-size: 27px;
    white-space: nowrap;
  }
  .contact-icon {
    width: 24px;
    height: 24px;
    margin-right: 19px;
    fill: var(--icon-blue);
    flex: none;
  }
</style>
</head>
<body>
<main class="card">
  <section class="brand">
    <div class="brand-square"></div>
    <div class="brand-name">RB Cargonet</div>
  </section>

  <div class="divider"></div>

  <header class="person">
    <h1 class="person-name">Varga Edina</h1>
    <p class="person-title">General Manager</p>
  </header>

  <ul class="contacts">
    <li class="contact-item">
      <svg class="contact-icon" viewBox="0 0 24 24" aria-hidden="true"><path d="M6.6 10.8c1.4 2.8 3.8 5.1 6.6 6.6l2.2-2.2c.3-.3.7-.4 1-.2 1.1.4 2.3.6 3.6.6.6 0 1 .4 1 1V20c0 .6-.4 1-1 1C10.6 21 3 13.4 3 4c0-.6.4-1 1-1h3.5c.6 0 1 .4 1 1 0 1.3.2 2.5.6 3.6.1.3 0 .7-.2 1z"/></svg>
      +36-70/482-5910
    </li>
    <li class="contact-item">
      <svg class="contact-icon" viewBox="0 0 24 24" aria-hidden="true"><rect x="2" y="7" width="5" height="15" rx="1"/><path d="M9 3h9l3 3v16H9z"/><rect x="11" y="12" width="2" height="2" fill="#000"/><rect x="15" y="12" width="2" height="2" fill="#000"/><rect x="11" y="16" width="2" height="2" fill="#000"/><rect x="15" y="16" width="2" height="2" fill="#000"/><rect x="11" y="6" width="6" height="3" fill="#000"/></svg>
      +36-1/655-3947
    </li>
    <li class="contact-item">
      <svg class="contact-icon" viewBox="0 0 24 24" aria-hidden="true"><path d="M2 5h20v14H2z M4 7v.6l8 5.4 8-5.4V7z" fill-rule="evenodd"/></svg>
      edina.varga@rbcargonet-example.com
    </li>
    <li class="contact-item">
      <svg class="contact-icon" viewBox="0 0 24 24" aria-hidden="true"><path d="M2 5h20v14H2z M4 7v.6l8 5.4 8-5.4V7z" fill-rule="evenodd"/></svg>
      info@rbcargonet-example.com
    </li>
    <li class="contact-item">
      <svg class="contact-icon" viewBox="0 0 24 24" aria-hidden="true"><path d="M10.6 13.4a1 1 0 0 1 0-1.4l4-4a1 1 0 1 1 1.4 1.4l-4 4a1 1 0 0 1-1.4 0zM8.5 20.5a5 5 0 0 1-3.5-8.5l2.5-2.5 1.4 1.4-2.5 2.5a3 3 0 0 0 4.2 4.2l2.5-2.5 1.4 1.4-2.5 2.5a5 5 0 0 1-3.5 1.5zM16.5 14.5l-1.4-1.4 2.5-2.5a3 3 0 0 0-4.2-4.2l-2.5 2.5-1.4-1.4 2.5-2.5a5 5 0 0 1 7 7z"/></svg>
      www.rbcargonet-example.com
    </li>
  </ul>
</main>
</body>
</html>
```